Verdant Orchard - Stationery Design Project

We need a stationary for our business. We grow roots and fruits in Central and South America, we import and distribute in FL, USA. We do fresh and frozen products.

Target Market(s)

Small and big supermarkets, wholesalers, traders, distributors, etc

Industry/Entity Type

Business

```html
<!DOCTYPE html>
<html lang="en">
<head>
<meta charset="utf-8">
<title>Verdant Orchard Stationery</title>
<link href="https://fonts.googleapis.com/css2?family=Montserrat:wght@500&display=swap" rel="stylesheet">
<style>
  :root {
    --orange: #e8820c;
    --green: #556335;
    --paper: #ffffff;
    --backdrop: #efebe4;
    --watermark: #dcdcd2;
    --shadow: rgba(60, 40, 20, 0.22);
  }
  * { box-sizing: border-box; margin: 0; padding: 0; }
  html, body { width: 901px; height: 1200px; overflow: hidden; }
  body {
    background: var(--backdrop);
    font-family: "Montserrat", sans-serif;
    position: relative;
  }
  .sheet {
    position: absolute;
    background: var(--paper);
    box-shadow: 0 3px 10px var(--shadow);
    overflow: hidden;
  }
  .brand-name {
    font-weight: 500;
    color: var(--green);
    white-space: nowrap;
    letter-spacing: 0.02em;
    text-transform: uppercase;
  }
  .header-band {
    position: absolute; left: 0; right: 0; top: 0;
    display: flex;
  }
  .header-band .band-orange { background: var(--orange); flex: 0 0 37%; }
  .header-band .band-logo {
    flex: 0 0 30%;
    display: flex; align-items: center; justify-content: center;
  }
  .header-band .band-green { background: var(--green); flex: 1; }
  .rule-pair { position: absolute; left: 0; right: 0; }
  .rule-pair span { display: block; height: 1.5px; }
  .rule-pair .rule-green { background: var(--green); margin-bottom: 3px; }
  .rule-pair .rule-orange { background: var(--orange); }
  .footer-wave { position: absolute; left: 0; bottom: 0; width: 100%; }

  /* Letterhead */
  .letterhead { left: 430px; top: 150px; width: 420px; height: 900px; }
  .letterhead .header-band { height: 55px; }
  .letterhead .brand-name { font-size: 10px; }
  .letterhead .rule-pair { top: 58px; }
  .letterhead .watermark {
    position: absolute; left: 0; right: 0; top: 440px;
    text-align: center;
    font-size: 30px; color: var(--watermark);
  }
  .letterhead .footer-wave { height: 40px; }

  /* Business cards */
  .card { width: 190px; height: 105px; }
  .card-front { left: 60px; top: 330px; }
  .card-front .top-band { position: absolute; left: 0; right: 0; top: 0; height: 15px; background: var(--green); }
  .card-front .bottom-band { position: absolute; left: 0; right: 0; bottom: 0; height: 17px; background: var(--orange); }
  .card-front .rule-line { position: absolute; left: 0; right: 0; bottom: 21px; height: 1px; background: var(--green); }
  .card-front .brand-name {
    position: absolute; left: 0; right: 0; top: 44px;
    text-align: center; font-size: 9px;
  }
  .card-back { left: 215px; top: 355px; }
  .card-back .corner-band { position: absolute; right: 0; top: 0; width: 58%; height: 17px; background: var(--orange); }
  .card-back .brand-name { position: absolute; left: 8px; top: 5px; font-size: 6px; }
  .card-back .bottom-band { position: absolute; left: 0; right: 0; bottom: 0; height: 9px; background: var(--green); }
  .card-back .rule-line { position: absolute; left: 0; right: 0; bottom: 12px; height: 1px; background: var(--green); }

  /* Envelope */
  .envelope { left: 40px; top: 650px; width: 440px; height: 215px; }
  .envelope .header-band { height: 40px; }
  .envelope .brand-name { font-size: 8px; }
  .envelope .rule-pair { top: 43px; }
  .envelope .footer-wave { height: 34px; }
</style>
</head>
<body>

  <section class="sheet letterhead" aria-label="Letterhead">
    <div class="header-band">
      <div class="band-orange"></div>
      <div class="band-logo"><span class="brand-name">Verdant Orchard</span></div>
      <div class="band-green"></div>
    </div>
    <div class="rule-pair"><span class="rule-green"></span><span class="rule-orange"></span></div>
    <div class="watermark brand-name">Verdant Orchard</div>
    <svg class="footer-wave" viewBox="0 0 420 40" preserveAspectRatio="none" aria-hidden="true">
      <path d="M0 14 Q210 -2 420 6 L420 40 L0 40 Z" fill="var(--orange)"/>
      <path d="M0 20 Q210 6 420 12 L420 40 L0 40 Z" fill="var(--green)"/>
    </svg>
  </section>

  <section class="sheet card card-front" aria-label="Business card front">
    <div class="top-band"></div>
    <span class="brand-name">Verdant Orchard</span>
    <div class="rule-line"></div>
    <div class="bottom-band"></div>
  </section>

  <section class="sheet card card-back" aria-label="Business card back">
    <div class="corner-band"></div>
    <span class="brand-name">Verdant Orchard</span>
    <div class="rule-line"></div>
    <div class="bottom-band"></div>
  </section>

  <section class="sheet envelope" aria-label="Envelope">
    <div class="header-band">
      <div class="band-orange"></div>
      <div class="band-logo"><span class="brand-name">Verdant Orchard</span></div>
      <div class="band-green"></div>
    </div>
    <div class="rule-pair"><span class="rule-green"></span><span class="rule-orange"></span></div>
    <svg class="footer-wave" viewBox="0 0 440 34" preserveAspectRatio="none" aria-hidden="true">
      <path d="M0 4 Q200 20 440 6 L440 34 L0 34 Z" fill="var(--orange)"/>
      <path d="M0 12 Q200 24 440 12 L440 34 L0 34 Z" fill="var(--green)"/>
    </svg>
  </section>

</body>
</html>
```